Need business card design for a confectionery company specializing in chocolates. Would like to see designs that use chocolate brown background and lime green wording and logo. Logo preferably chocolate-related.

Target Market(s)

Corporate, Gifts & Occasions, Hotels, Supermarkets, Parties, Events, Weddings

Industry/Entity Type

Food Production

Contact Information for Business Card

Velbrook Confectionery (company name on front of card in lime green)
with words beneath company name saying "handmade sweets for each celebration" (in lime green in lower case)

Font styles to use
Script

Colors
acd037

Requirements
Must have
• Front of card: Brown background
• Back of card: White background
• Email address on back of card: Info@velbrook.example.zw
• Cellphone number on back of card: 0771 392 615, 0773 581 246
• Address on back of card: 8 Tarnby Close, Marlow Rise, Harare
• ALL WRITING ON BACK OF CARD IN BLACK

```html
<!DOCTYPE html>
<html lang="en">
<head>
<meta charset="utf-8">
<title>Velbrook Confectionery – Business Cards</title>
<link rel="stylesheet" href="https://fonts.googleapis.com/css2?family=Dancing+Script:wght@500;600&display=swap">
<style>
  :root {
    --page-bg: #e9e7e4;
    --card-white: #ffffff;
    --card-brown: #361a14;
    --lime: #acd037;
    --ink: #1a1a1a;
    --rule: #2a2a2a;
  }
  * { box-sizing: border-box; margin: 0; padding: 0; }
  html, body {
    width: 1200px; height: 901px; overflow: hidden;
    background: var(--page-bg);
  }
  .canvas { position: relative; width: 1200px; height: 901px; }
  .card {
    position: absolute; width: 620px; height: 354px;
    box-shadow: 0 6px 18px rgba(0,0,0,0.18);
    font-family: "Dancing Script", cursive;
    font-weight: 500;
  }
  .card--back { left: 60px; top: 80px; background: var(--card-white); color: var(--ink); }
  .card--front { left: 520px; top: 467px; background: var(--card-brown); color: var(--lime); }

  .company-name { color: var(--lime); font-weight: 500; line-height: 1.1; }
  .tagline { color: var(--lime); font-weight: 500; line-height: 1.1; }

  .back-brand { position: absolute; right: 40px; top: 26px; text-align: right; }
  .back-brand .company-name { font-size: 28px; }
  .back-brand .tagline { font-size: 19px; margin-top: 2px; }

  .holder { position: absolute; right: 40px; top: 102px; text-align: right; }
  .holder__name { font-size: 24px; line-height: 1.1; }
  .holder__role { font-size: 13px; line-height: 1.2; margin-top: 6px; }
  .rule { position: absolute; left: 24px; right: 40px; height: 1px; background: var(--rule); }
  .rule--top { top: 134px; right: 80px; }
  .rule--bottom { top: 248px; }

  .contacts { position: absolute; left: 28px; top: 258px; list-style: none; }
  .contacts li {
    display: flex; align-items: center; gap: 10px;
    font-size: 18px; line-height: 28px;
  }
  .contacts svg { width: 15px; height: 15px; flex: none; }

  .front-brand { position: absolute; left: 0; right: 0; top: 108px; text-align: center; }
  .front-brand .company-name { font-size: 36px; }
  .front-brand .tagline { font-size: 24px; margin-top: 6px; }

  .markets {
    position: absolute; left: 20px; right: 20px; bottom: 30px;
    display: flex; justify-content: space-between; list-style: none;
    font-size: 17px;
  }
  .markets li::before { content: "• "; color: #ffffff; }
</style>
</head>
<body>
<main class="canvas">
  <section class="card card--back" aria-label="Back of card">
    <div class="back-brand">
      <p class="company-name">Velbrook Confectionery</p>
      <p class="tagline">handmade sweets for each celebration</p>
    </div>
    <div class="holder">
      <p class="holder__name">Rudo Marara</p>
      <p class="holder__role">CEO</p>
    </div>
    <div class="rule rule--top"></div>
    <div class="rule rule--bottom"></div>
    <ul class="contacts">
      <li>
        <svg viewBox="0 0 16 16" aria-hidden="true"><circle cx="8" cy="8" r="7" fill="none" stroke="#1a1a1a" stroke-width="1.2"/><path d="M5 4.5l1.5-.5 1 2-1 .8c.5 1 1.2 1.7 2.2 2.2l.8-1 2 1-.5 1.5c-3 .3-6.3-3-6-6z" fill="#1a1a1a"/></svg>
        0771 392 615, 0773 581 246
      </li>
      <li>
        <svg viewBox="0 0 16 16" aria-hidden="true"><rect x="1.5" y="3.5" width="13" height="9" fill="none" stroke="#1a1a1a" stroke-width="1.2"/><path d="M1.5 3.5l6.5 5 6.5-5" fill="none" stroke="#1a1a1a" stroke-width="1.2"/></svg>
        Info@velbrook.example.zw
      </li>
      <li>
        <svg viewBox="0 0 16 16" aria-hidden="true"><path d="M8 15s-5-5.2-5-8.5a5 5 0 0 1 10 0C13 9.8 8 15 8 15z" fill="none" stroke="#1a1a1a" stroke-width="1.2"/><circle cx="8" cy="6.5" r="1.8" fill="#1a1a1a"/></svg>
        8 Tarnby Close, Marlow Rise, Harare
      </li>
    </ul>
  </section>

  <section class="card card--front" aria-label="Front of card">
    <div class="front-brand">
      <p class="company-name">Velbrook Confectionery</p>
      <p class="tagline">handmade sweets for each celebration</p>
    </div>
    <ul class="markets">
      <li>Gifts &amp; Occasions</li>
      <li>Hotels</li>
      <li>Corporate</li>
      <li>Supermarkets</li>
      <li>Events</li>
      <li>Weddings</li>
      <li>Parties</li>
    </ul>
  </section>
</main>
</body>
</html>
```